Business Card Design Project

I need a new business card design for my Remodel/Design/Build company, Northgate Home Improvement, Inc. See our website: www.northgatehomeimprovement-example.com
We are an established company with a growing reputation and growing quickly. We are know for being on the forward edge of the industry, producing a great product and our "people friendly" approach.
I am looking for something cool, transitional, maybe even retro that captures the imagination, shows our sleek creativity and streamlined approach as well as communicates stability and trustworthiness.
Updates

Stainless steel business card design would be cool.

Please have all future designs with full logo colors and shown on a stainless steel business card.  Also, logo and tag line will most likely be printed with spot uv, so layers will be necessary.  Thank you.

Target Market(s)

30-65 yrs old, homeowners, appreciate fine things, median income $150+k, net worth $1+m

Industry/Entity Type

Business

Requirements
Must have
• Company Logo
Contact information
Website URL
Nice to have
• Tagline: Building Relationships and Remodeling Homes...One Client at a Time.
Double-sided okay.
Stainless steel business card.

```html
<!DOCTYPE html>
<html lang="en">
<head>
<meta charset="utf-8">
<title>Northgate Home Improvement – Business Card</title>
<link rel="stylesheet" href="https://fonts.googleapis.com/css2?family=Open+Sans:wght@400;600&family=Orbitron:wght@500&family=Montserrat:wght@500&display=swap">
<style>
  :root {
    --page: #ffffff;
    --label: #1a1a1a;
    --card-dark: #0c0c0c;
    --card-mid: #2e2e2e;
    --card-light: #4a4a4a;
    --text: #f4f4f4;
    --brand-grey: #c9c9c9;
    --brand-red: #9c1414;
    --phone-green: #6cbf2a;
    --phone-green-dark: #3f8f12;
    --icon-blue: #3a7fd0;
    --icon-blue-dark: #1f4f96;
  }
  * { margin: 0; padding: 0; box-sizing: border-box; }
  html, body { width: 811px; height: 1200px; overflow: hidden; background: var(--page); }
  body { position: relative; font-family: "Open Sans", Arial, sans-serif; }

  .side-label {
    position: absolute; left: 0; width: 811px; text-align: center;
    font-size: 30px; color: var(--label); font-weight: 400;
  }
  .side-label--front { top: -4px; }
  .side-label--back { top: 618px; }

  .card {
    position: absolute;
    background: radial-gradient(ellipse at 55% 45%, var(--card-light) 0%, var(--card-mid) 35%, var(--card-dark) 100%);
    color: var(--text);
    overflow: hidden;
  }
  .card--front { left: 6px; top: 99px; width: 802px; height: 466px; }
  .card--back { left: 0; top: 710px; width: 806px; height: 470px;
    background: radial-gradient(ellipse at 50% 50%, #262626 0%, #161616 60%, var(--card-dark) 100%); }

  .brand-mark { position: absolute; left: 40px; top: 58px; width: 150px; height: 150px; }
  .brand-name {
    position: absolute; left: 200px; top: 52px;
    font-family: "Montserrat", Arial, sans-serif; font-weight: 500;
    color: var(--brand-grey); letter-spacing: 5px; line-height: 1.2;
    font-size: 34px; text-transform: uppercase;
  }
  .holder-name { position: absolute; left: 283px; top: 186px; font-size: 27px; font-weight: 400; }

  .tagline {
    position: absolute; font-family: "Orbitron", Arial, sans-serif; font-weight: 500;
    font-size: 21px; color: var(--text); letter-spacing: 1px; white-space: nowrap;
  }
  .tagline--first { left: 70px; top: 330px; }
  .tagline--second { right: 58px; top: 363px; }

  .contact-row { position: absolute; display: flex; align-items: center; white-space: nowrap; }
  .contact-row svg { flex: none; }
  .phones { left: 234px; top: 152px; }
  .phones .numbers { margin-left: 11px; font-size: 27px; line-height: 38px; }
  .email { left: 103px; top: 318px; font-size: 24px; }
  .web { left: 140px; top: 362px; font-size: 24px; }
  .email span, .web span { margin-left: 8px; }
</style>
</head>
<body>
  <div class="side-label side-label--front">front</div>

  <section class="card card--front" role="img" aria-label="Front of card on a dark brushed-metal honeycomb texture">
    <svg class="brand-mark" viewBox="0 0 150 150" aria-hidden="true">
      <circle cx="75" cy="75" r="70" fill="var(--brand-red)" stroke="#ffffff" stroke-width="4"/>
    </svg>
    <div class="brand-name">Northgate<br>Home Improvement</div>
    <div class="holder-name">Dana Whitlock ( President )</div>
    <p class="tagline tagline--first">We Earn Your Trust and Renew Your Spaces</p>
    <p class="tagline tagline--second">Every Project with Care....</p>
  </section>

  <div class="side-label side-label--back">back</div>

  <section class="card card--back" role="img" aria-label="Back of card on a dark brushed-metal honeycomb texture">
    <div class="contact-row phones">
      <svg width="56" height="58" viewBox="0 0 56 58" aria-hidden="true">
        <defs>
          <linearGradient id="phoneTile" x1="0" y1="0" x2="0" y2="1">
            <stop offset="0" stop-color="var(--phone-green)"/>
            <stop offset="1" stop-color="var(--phone-green-dark)"/>
          </linearGradient>
        </defs>
        <rect x="1" y="1" width="54" height="56" rx="10" fill="url(#phoneTile)"/>
        <path d="M19 14c2-1 4 0 5 2l2 5c1 2 0 3-1 4l-2 2c1 4 5 8 9 9l2-2c1-1 2-2 4-1l5 2c2 1 3 3 2 5l-2 3c-1 2-4 3-7 2-10-3-17-10-20-20-1-3 0-6 3-8z" fill="#ffffff"/>
      </svg>
      <div class="numbers">Office : 760-555-0162<br>Mobile: 760-555-0188</div>
    </div>

    <div class="contact-row email">
      <svg width="38" height="37" viewBox="0 0 38 37" aria-hidden="true">
        <rect x="1" y="1" width="36" height="35" rx="6" fill="var(--icon-blue)" stroke="var(--icon-blue-dark)"/>
        <rect x="8" y="11" width="22" height="15" fill="#ffffff"/>
        <path d="M8 11l11 9 11-9" fill="none" stroke="var(--icon-blue-dark)" stroke-width="2"/>
      </svg>
      <span>dana@northgatehomeimprovement-example.com</span>
    </div>

    <div class="contact-row web">
      <svg width="38" height="38" viewBox="0 0 38 38" aria-hidden="true">
        <rect x="1" y="1" width="36" height="36" rx="6" fill="var(--icon-blue)" stroke="var(--icon-blue-dark)"/>
        <circle cx="19" cy="19" r="11" fill="none" stroke="#ffffff" stroke-width="2"/>
        <ellipse cx="19" cy="19" rx="5" ry="11" fill="none" stroke="#ffffff" stroke-width="1.5"/>
        <line x1="8" y1="19" x2="30" y2="19" stroke="#ffffff" stroke-width="1.5"/>
      </svg>
      <span>www.northgatehomeimprovement-example.com</span>
    </div>
  </section>
</body>
</html>
```